Business card design needed

New company based in Brisbane, Australia. Brindle Systems. The business is focused on the delivery of network architecture design and deployment. We will provide both services and the sale of the necessary equipment to deliver the service. Cloud computing is an important element of our focus as this is an emerging market for enterprises in Queensland. Our target marketplace is medium to large corporations with complex infrastructure requirements. IT Management and above will be the typical entry point for us into these accounts. We would like to see the use of various shade of green, design should be clutter free and impress stability, trust and growth.
Updates
Hey Everyone
Just we let you all know we have changed this project to 'committed' payment status.
Looking forward to seeing the designs! Thanks for your efforts.
Best Regards
Marcus
Industry/Entity Type
Architecture
Contact Information for Business Card
Brindle Systems, Marcus Doyle, Sales Director, Level 14 Harlow Tower, 58 Penfold Street, Brisbane QLD 4000, Ph +61 7 3904 2267, M +61 4 4926 1573, E marcus.doyle@brindlesystems-example.com.au
Look and feel
Each slider illustrates characteristics of the customer's brand and the style your logo design should communicate.

```html
<!DOCTYPE html>
<html lang="en">
<head>
<meta charset="utf-8">
<title>Brindle Systems – Business Card</title>
<link href="https://fonts.googleapis.com/css2?family=PT+Sans:wght@400;700&display=swap" rel="stylesheet">
<style>
  :root {
    --page-bg: #ece9e3;
    --card-green: #013c1f;
    --card-green-deep: #002e17;
    --card-green-glow: #0f7042;
    --band-dark: #0b2115;
    --ink-light: #ffffff;
    --ink-soft: #dfeee5;
    --icon-glyph: #0b4a29;
  }
  * { box-sizing: border-box; margin: 0; padding: 0; }
  html, body { width: 1200px; height: 1000px; overflow: hidden; }
  body {
    background: var(--page-bg);
    font-family: "PT Sans", "Segoe UI", sans-serif;
    color: var(--ink-light);
    position: relative;
  }
  .card {
    position: absolute;
    top: 349px;
    width: 564px;
    height: 302px;
    box-shadow: 0 3px 8px rgba(0,0,0,0.35);
    overflow: hidden;
  }
  /* Contact side */
  .card--contact { left: 46px; background: var(--card-green); }
  .contact-band {
    position: absolute; right: 0; top: 0; bottom: 0; width: 93px;
    background: var(--band-dark);
  }
  .contact-band__name {
    position: absolute; left: 50%; top: 50%;
    transform: translate(-50%, -50%) rotate(-90deg);
    white-space: nowrap;
    font-size: 24px; font-weight: 400; letter-spacing: 0.3px;
    color: var(--ink-light);
  }
  .holder { position: absolute; left: 25px; top: 24px; }
  .holder__row { display: flex; align-items: center; gap: 8px; }
  .holder__mark {
    width: 24px; height: 24px; border-radius: 50%;
    border: 2px solid var(--ink-light);
  }
  .holder__name { font-size: 21px; font-weight: 700; }
  .holder__role { margin: 6px 0 0 74px; font-size: 14px; color: var(--ink-soft); }
  .contact-list { position: absolute; left: 24px; top: 170px; list-style: none; }
  .contact-list li {
    display: flex; align-items: flex-start; gap: 7px;
    font-size: 14.5px; line-height: 17px; margin-bottom: 8px;
  }
  .contact-list svg { flex: 0 0 20px; width: 20px; height: 20px; margin-top: -1px; }
  /* Brand side */
  .card--brand {
    left: 617px;
    background: radial-gradient(ellipse 60% 75% at 50% 42%, var(--card-green-glow) 0%, var(--card-green) 62%, var(--card-green-deep) 100%);
  }
  .brand-rule {
    position: absolute; left: 73px; width: 390px; height: 1px;
    background: linear-gradient(90deg, rgba(255,255,255,0), rgba(255,255,255,0.85) 50%, rgba(255,255,255,0));
  }
  .brand-rule--top { top: 64px; }
  .brand-rule--bottom { top: 238px; }
  .brand-lockup {
    position: absolute; left: 0; right: 0; top: 122px; text-align: center;
  }
  .brand-lockup__name { font-size: 36px; font-weight: 400; line-height: 38px; }
  .brand-lockup__web { font-size: 13px; color: var(--ink-soft); margin-left: 52px; }
</style>
</head>
<body>

<section class="card card--contact" aria-label="Business card, contact side">
  <div class="holder">
    <div class="holder__row">
      <span class="holder__mark"></span>
      <span class="holder__name">Marcus Doyle</span>
    </div>
    <p class="holder__role">sales director</p>
  </div>

  <ul class="contact-list">
    <li>
      <svg viewBox="0 0 20 20" aria-hidden="true"><circle cx="10" cy="10" r="9.5" fill="#fff"/><rect x="6.5" y="3.5" width="7" height="13" rx="1.3" fill="none" stroke="var(--icon-glyph)" stroke-width="1.4"/><rect x="8" y="5.5" width="4" height="5" fill="var(--icon-glyph)"/></svg>
      <span>+61 4 4926 1573</span>
    </li>
    <li>
      <svg viewBox="0 0 20 20" aria-hidden="true"><circle cx="10" cy="10" r="9.5" fill="#fff"/><path d="M6 4.5c-1 .6-1.6 1.8-1 3.4 1.2 3.3 4 6.1 7.3 7.3 1.6.5 2.8 0 3.4-1l-2.2-2.2-1.6 1c-1.5-.8-2.7-2-3.5-3.5l1-1.6z" fill="var(--icon-glyph)"/></svg>
      <span>+61 7 3904 2267</span>
    </li>
    <li>
      <svg viewBox="0 0 20 20" aria-hidden="true"><circle cx="10" cy="10" r="9.5" fill="#fff"/><rect x="4.5" y="6" width="11" height="8" fill="var(--icon-glyph)"/><path d="M4.5 6l5.5 4.5L15.5 6" fill="none" stroke="#fff" stroke-width="1.1"/></svg>
      <span>marcus.doyle@brindlesystems-example.com.au</span>
    </li>
    <li>
      <svg viewBox="0 0 20 20" aria-hidden="true"><circle cx="10" cy="10" r="9.5" fill="#fff"/><path d="M10 4L3.8 9.6h1.8V15h3.3v-3.3h2.2V15h3.3V9.6h1.8z" fill="var(--icon-glyph)"/></svg>
      <span>Level 14 Harlow Tower, 58 Penfold Street,<br>Brisbane QLD 4000</span>
    </li>
  </ul>

  <div class="contact-band">
    <span class="contact-band__name">Brindle Systems</span>
  </div>
</section>

<section class="card card--brand" aria-label="Business card, brand side">
  <div class="brand-rule brand-rule--top"></div>
  <div class="brand-lockup">
    <p class="brand-lockup__name">Brindle Systems</p>
    <p class="brand-lockup__web">brindlesystems-example.com.au</p>
  </div>
  <div class="brand-rule brand-rule--bottom"></div>
</section>

</body>
</html>
```